2 x Digitize Logo | 2 x Business Cards | 2 x Fridge Magnets

We require 6 deliverables:
1. Residential logo redrawn (same just high quality for large print format).
2. Corporate logo redrawn (minor changes to wording and high quality for large print format).
3. New business card design for Furniture Removals (residential)
4. New business card design for Corporate Relocations (business)
5. New Fridge magnet for Furniture removals (residential)
6. New fridge magnet for Corporate Relocations (business)
1. Residential Logo
a. We require the logo to be translated into a high quality digital image with no modifications.
(see attached resilogo.jpg)
2. Residential Logo
a. We require the logo to be edited (add the word corporate relocations) be translated into a high quality digital image.
(see attached corplogo.jpg)
3. Using the resilogo please make a new business card for our business.
a. Please see the web site https://www.bluegatehaulage.com.au for colours and inspiration.
b. The residential business card needs the following information:
i. Business Name (using the residential logo).
ii. Free Call: 1800 BG Haul (the B, G and Haul much be the same colour as the logo).
iii. Website: www.BluegateHaulage.com.au
iv. Address: 4/6 Marlow Court, VIC 3201
v. Email: move@BluegateHaulage.com.au
vi. backof Card:
Review our service
www.TellTallyHub.com.au
Services: Local, Country, Interstate | Furniture Removals | Piano, Billiard Tables & Antiques
4. Using the corplogo please make a new business card for our business.
b. The corporate business card needs the following information:
i. Business Name (using the corporate logo).
v. Email: corporate@BluegateHaulage.com.au
vi. Back of Card:
Review our service
www.TellTallyHub.com.au
Services: Corporate relocations | Office equipment moves | Packing Service | Packing Materials
5. Using the resilogo please make a new fridge magent for our business.
b. The residential fidge magnet needs the following information:
iv. Services: Local, Country, Interstate | Furniture Removals | Piano, Billiard Tables & Antiques
6. Using the corplogo please make a new fridge magent for our business.
b. The corporate fidge magnet needs the following information:
iv. Services: Local, Country, Interstate | Corporate relocations
Target Market(s)
Residential Furniture Removals and Corporate Office relocations
Industry/Entity Type
Business
Contact Information for Business Card
Please see full brief for six items required
Requirements
Must have
- Clean simple, easy to read
Nice to have
- fresh, stand out, eye catching
Should not have
- plain, standard, boring, general

```html
<!DOCTYPE html>
<html lang="en">
<head>
<meta charset="utf-8">
<title>Bluegate Haulage – Corporate Business Card</title>
<link rel="stylesheet" href="https://fonts.googleapis.com/css2?family=Open+Sans:wght@400;600&family=Oswald:wght@500;700&display=swap">
<style>
  :root {
    --page-bg: #e9e6e1;
    --card-bg: #ffffff;
    --brand-yellow: #f2c21a;
    --brand-red: #e02b2b;
    --brand-green: #22b04b;
    --ink: #4a4a4a;
    --ink-soft: #6b6b6b;
    --shadow: rgba(0, 0, 0, 0.18);
  }
  * { box-sizing: border-box; margin: 0; padding: 0; }
  html, body { width: 771px; height: 1200px; overflow: hidden; }
  body {
    background: var(--page-bg);
    font-family: "Open Sans", Arial, sans-serif;
    color: var(--ink);
    position: relative;
  }
  .card {
    position: absolute;
    left: 65px;
    width: 640px;
    height: 366px;
    background: var(--card-bg);
    box-shadow: 0 8px 24px var(--shadow);
    overflow: hidden;
  }
  .card--front { top: 170px; }
  .card--back { top: 660px; }
  .card__bands { position: absolute; inset: 0; width: 100%; height: 100%; }

  .brand-name {
    position: absolute;
    font-family: "Oswald", "Arial Narrow", sans-serif;
    font-weight: 700;
    letter-spacing: 1px;
    color: var(--brand-green);
    text-transform: uppercase;
    white-space: nowrap;
    line-height: 1.2;
  }
  .card--front .brand-name { top: 78px; left: 300px; font-size: 28px; }
  .card--back .brand-name { top: 96px; right: 40px; font-size: 38px; }

  .holder { position: absolute; left: 40px; top: 150px; }
  .holder__name { font-size: 26px; font-weight: 400; color: var(--ink-soft); }
  .holder__role { font-size: 13px; color: var(--brand-red); margin-top: 2px; }

  .free-call {
    position: absolute; left: 40px; top: 222px;
    font-family: "Oswald", "Arial Narrow", sans-serif;
    font-weight: 500; font-size: 22px; color: var(--brand-yellow);
  }
  .free-call__number { color: var(--brand-red); font-weight: 700; }

  .contact-list { position: absolute; left: 40px; top: 262px; list-style: none; }
  .contact-list__item {
    display: flex; align-items: center; gap: 8px;
    font-size: 13px; color: var(--ink-soft); line-height: 24px;
  }
  .contact-list__item--web { color: var(--brand-green); }
  .contact-list__icon { width: 14px; height: 14px; flex: none; }

  .services { position: absolute; left: 40px; top: 196px; }
  .services__title { font-size: 14px; color: var(--brand-yellow); margin-bottom: 4px; }
  .services__list { list-style: none; }
  .services__item {
    display: flex; align-items: center; gap: 10px;
    font-size: 16px; color: var(--ink); line-height: 28px;
  }
  .services__tick { width: 16px; height: 16px; flex: none; }

  .review { position: absolute; left: 300px; bottom: 34px; }
  .review__label { font-size: 13px; color: var(--brand-green); }
  .review__url { font-size: 14px; color: var(--ink); }
</style>
</head>
<body>

<section class="card card--front" aria-label="Business card front">
  <svg class="card__bands" viewBox="0 0 640 366" preserveAspectRatio="none" aria-hidden="true">
    <polygon points="0,0 470,0 0,70" fill="var(--brand-yellow)"/>
    <polygon points="600,0 640,0 640,80 500,366 430,366" fill="var(--brand-green)"/>
    <polygon points="521,170 430,366 340,366" fill="var(--brand-red)"/>
  </svg>

  <div class="brand-name">Bluegate Haulage</div>

  <div class="holder">
    <p class="holder__name">Your Name</p>
    <p class="holder__role">Position</p>
  </div>

  <p class="free-call">Free Call: <span class="free-call__number">1800 BG Haul</span></p>

  <ul class="contact-list">
    <li class="contact-list__item">
      <svg class="contact-list__icon" viewBox="0 0 14 14" aria-hidden="true">
        <path d="M7 1a4 4 0 0 0-4 4c0 3 4 8 4 8s4-5 4-8a4 4 0 0 0-4-4z" fill="var(--brand-green)"/>
        <circle cx="7" cy="5" r="1.5" fill="#fff"/>
      </svg>
      4/6 Marlow Court, VIC 3201
    </li>
    <li class="contact-list__item">
      <svg class="contact-list__icon" viewBox="0 0 14 14" aria-hidden="true">
        <rect x="1" y="3" width="12" height="8" fill="var(--brand-green)"/>
        <polyline points="1,3 7,8 13,3" fill="none" stroke="#fff" stroke-width="1"/>
      </svg>
      corporate@BluegateHaulage.com.au
    </li>
    <li class="contact-list__item contact-list__item--web">www.BluegateHaulage.com.au</li>
  </ul>
</section>

<section class="card card--back" aria-label="Business card back">
  <svg class="card__bands" viewBox="0 0 640 366" preserveAspectRatio="none" aria-hidden="true">
    <polygon points="0,0 330,0 0,150" fill="var(--brand-yellow)"/>
    <polygon points="330,0 380,0 0,175 0,150" fill="var(--brand-red)"/>
    <polygon points="380,0 430,0 0,198 0,175" fill="var(--brand-green)"/>
  </svg>

  <div class="brand-name">Bluegate Haulage</div>

  <div class="services">
    <p class="services__title">Services</p>
    <ul class="services__list">
      <li class="services__item"><svg class="services__tick" viewBox="0 0 16 16" aria-hidden="true"><rect x="1" y="3" width="11" height="11" fill="none" stroke="var(--brand-red)" stroke-width="1.5"/><polyline points="4,8 7,11 15,1" fill="none" stroke="var(--brand-red)" stroke-width="2"/></svg>Corporate relocations</li>
      <li class="services__item"><svg class="services__tick" viewBox="0 0 16 16" aria-hidden="true"><rect x="1" y="3" width="11" height="11" fill="none" stroke="var(--brand-red)" stroke-width="1.5"/><polyline points="4,8 7,11 15,1" fill="none" stroke="var(--brand-red)" stroke-width="2"/></svg>Office equipment moves</li>
      <li class="services__item"><svg class="services__tick" viewBox="0 0 16 16" aria-hidden="true"><rect x="1" y="3" width="11" height="11" fill="none" stroke="var(--brand-red)" stroke-width="1.5"/><polyline points="4,8 7,11 15,1" fill="none" stroke="var(--brand-red)" stroke-width="2"/></svg>Packing Service</li>
      <li class="services__item"><svg class="services__tick" viewBox="0 0 16 16" aria-hidden="true"><rect x="1" y="3" width="11" height="11" fill="none" stroke="var(--brand-red)" stroke-width="1.5"/><polyline points="4,8 7,11 15,1" fill="none" stroke="var(--brand-red)" stroke-width="2"/></svg>Packing Materials</li>
    </ul>
  </div>

  <div class="review">
    <p class="review__label">Review our service</p>
    <p class="review__url">www.TellTallyHub.com.au</p>
  </div>
</section>

</body>
</html>
```